family chiropractic health care team needs a modern business card design

Healthcare office with Chiropractors, Physiotherapists, Massage therapists and possibly other practitioners in the future. This is a friendly family office with patients of all ages (and lots of kids) that just moved into a new larger modern office.
Look at the website for photos of the office.
Design for the front and back of a business card required.
Text for the front:
Office logo and name of the office:
Bright Path Wellness Centre
Name of current Practitioner:
Dr. Marten Quovel B.Sc., D.C. Chiropractor
(But please include options to swap out name and title for other practitioners )

address:
218 Farrow Gate
Etobicoke ON.
K2J 6P4
Phone: 416-872-0196 (PATH)
Web site and email:
www.brightpathwellnesscentre.example
brightpathchiro@mailbox.example

2 versions of the back of the card:
1. text below
2. appointment schedule card

Text on back of card:
Chiropractic Card text on back of the card:
There is more to chiropractic than the relief of headaches and back pain! Our primary focus is the integrity of your nerve system, which controls and regulates every cell and tissue of your body. The moving bones of the spinal column can impair this vital communication link between your brain and body. We help improve the function and structure of your spine, reducing nerve system compromise. The result?
Even non-spinal related health problems can show improvement
without drugs
without surgery
regardless of age
for over a century
naturally

Appointment Card info For Back:
Please integrate design elements from the front of the card into an appointment card format.
M Tu W Th F Sat (and a line for writing on beside each one)

```html
<!DOCTYPE html>
<html lang="en">
<head>
<meta charset="utf-8">
<title>Bright Path Wellness Centre – Business Card</title>
<link href="https://fonts.googleapis.com/css2?family=Roboto:wght@400;500;700&display=swap" rel="stylesheet">
<style>
  :root {
    --leaf-green: #8dc04b;
    --slate-grey: #7b7b7d;
    --ink: #222222;
    --paper: #ffffff;
    --backdrop: #c9c9c9;
    --symbol-soft: #e6f0d8;
    --symbol-deep: #b9d694;
  }
  * { box-sizing: border-box; margin: 0; padding: 0; }
  html, body {
    width: 1200px; height: 896px; overflow: hidden;
    background: var(--backdrop);
    font-family: "Roboto", Arial, sans-serif;
  }
  .canvas { position: relative; width: 1200px; height: 896px; }
  .card {
    position: absolute; left: 334px; width: 527px; height: 301px;
    background: var(--paper);
    box-shadow: 0 12px 18px rgba(0,0,0,0.18);
    overflow: hidden;
  }
  .card--front { top: 125px; }
  .card--back { top: 474px; }

  /* Front */
  .brand-symbol-area {
    position: absolute; left: 0; top: 0; width: 250px; height: 301px;
    background: radial-gradient(ellipse at 45% 40%, var(--symbol-deep) 0%, var(--symbol-soft) 60%, var(--paper) 100%);
  }
  .front-brand {
    position: absolute; right: 20px; top: 52px;
    display: flex; align-items: center; gap: 8px;
    color: var(--leaf-green); font-weight: 700; font-size: 19px; line-height: 1.1;
    text-align: right;
  }
  .brand-dot { width: 14px; height: 14px; border-radius: 50%; background: var(--leaf-green); flex: none; }
  .practitioner { position: absolute; right: 20px; top: 132px; text-align: right; }
  .practitioner__name { color: var(--leaf-green); font-weight: 700; font-size: 18px; }
  .practitioner__title { color: var(--ink); font-size: 13px; margin-top: 3px; }
  .accent-bar { position: absolute; right: 0; top: 135px; width: 12px; height: 34px; background: var(--leaf-green); }
  .contact-list { position: absolute; right: 20px; top: 186px; list-style: none; text-align: right; }
  .contact-list li {
    display: flex; justify-content: flex-end; align-items: center; gap: 7px;
    color: var(--ink); font-size: 12.5px; height: 17.5px;
  }
  .contact-list svg { width: 11px; height: 11px; fill: var(--leaf-green); flex: none; }
  .address { position: absolute; right: 20px; top: 250px; text-align: right; color: var(--ink); font-size: 12.5px; line-height: 17.5px; }

  /* Back */
  .back-brand {
    position: absolute; left: 0; right: 0; top: 80px;
    display: flex; justify-content: center; align-items: center; gap: 12px;
    color: var(--leaf-green); font-weight: 700; font-size: 30px;
  }
  .back-brand .brand-dot { width: 20px; height: 20px; }
  .appointment { position: absolute; left: 32px; right: 32px; top: 198px; color: var(--leaf-green); font-size: 13.5px; }
  .appointment__row { display: flex; align-items: baseline; height: 29px; }
  .fill-line { flex: 1; border-bottom: 2px dotted var(--leaf-green); margin: 0 2px; transform: translateY(-3px); }
  .fill-line--time { flex: 0 0 52px; }
  .weekdays { display: flex; justify-content: space-between; list-style: none; margin-top: 2px; }
  .weekdays li { display: flex; align-items: center; gap: 4px; }
  .tick-box { width: 16px; height: 10px; border: 1.2px solid var(--leaf-green); }
</style>
</head>
<body>
<main class="canvas">
  <section class="card card--front" aria-label="Business card front">
    <div class="brand-symbol-area" role="img" aria-label="Large brand symbol decoration area in green and grey"></div>

    <div class="front-brand">
      <span class="brand-dot"></span>
      <span>Bright Path<br>Wellness Centre</span>
    </div>

    <div class="practitioner">
      <p class="practitioner__name">Dr. Marten Quovel</p>
      <p class="practitioner__title">B.Sc., D.C. Chiropractor</p>
    </div>
    <div class="accent-bar"></div>

    <ul class="contact-list">
      <li>416-872-0196 (PATH)
        <svg viewBox="0 0 24 24" aria-hidden="true"><path d="M2 9c0-3 4-5 10-5s10 2 10 5v2h-5V9c-1-1-3-1.5-5-1.5S8 8 7 9v2H2zM6 12l3-3h6l3 3 2 8H4z"/></svg>
      </li>
      <li>brightpathchiro@mailbox.example
        <svg viewBox="0 0 24 24" aria-hidden="true"><path d="M2 5h20v3l-10 6L2 8zM2 10l10 6 10-6v9H2z"/></svg>
      </li>
      <li>www.brightpathwellnesscentre.example
        <svg viewBox="0 0 24 24" aria-hidden="true"><circle cx="12" cy="12" r="10"/></svg>
      </li>
    </ul>

    <p class="address">218 Farrow Gate<br>Etobicoke ON. K2J 6P4</p>
  </section>

  <section class="card card--back" aria-label="Appointment card back">
    <div class="back-brand">
      <span class="brand-dot"></span>
      <span>Bright Path Wellness Centre</span>
    </div>

    <div class="appointment">
      <div class="appointment__row"><span>Name:</span><span class="fill-line"></span></div>
      <div class="appointment__row">
        <span>Date:</span><span class="fill-line"></span>
        <span>Time:</span><span class="fill-line fill-line--time"></span><span>AM/PM</span>
      </div>
      <ul class="weekdays">
        <li>Mon.<span class="tick-box"></span></li>
        <li>Tue.<span class="tick-box"></span></li>
        <li>Wed.<span class="tick-box"></span></li>
        <li>Thu.<span class="tick-box"></span></li>
        <li>Fri.<span class="tick-box"></span></li>
        <li>Sat.<span class="tick-box"></span></li>
      </ul>
    </div>
  </section>
</main>
</body>
</html>
```